Poster design needed for Pregnant class 25.11.2018*

We need a poster design with the instruction details:
- Size: A4- Content:
1. Logo
2. Title of poster: Pregnant class - Eating healthy while pregnant
3. Promote when join in out class: 30% off delivery package
4. Singapore - 25.11.2018
5. Detail of contact: please visit https://www.harbourvalehospital.com.sg/And get information for this poster.

Pregnant

Medical And Science

Sans Serif

85cae6
33a6d7

• Picture mom and baby or pregnant

```html
<!DOCTYPE html>
<html lang="en">
<head>
<meta charset="utf-8">
<title>Pregnant Class Poster</title>
<link rel="stylesheet" href="https://fonts.googleapis.com/css2?family=Roboto+Slab:wght@400;500;700&family=Lexend:wght@500&family=Roboto+Condensed:wght@700&family=Roboto:wght@400;500&display=swap">
<style>
  :root {
    --backdrop: #3a3d40;
    --sky-light: #eef7fe;
    --sky-mid: #dcecf9;
    --sky-deep: #9fc2e3;
    --brand-blue: #33a6d7;
    --brand-blue-dark: #2a8fc4;
    --ink: #1b1b1b;
    --gold: #b2a67c;
    --white: #ffffff;
    --blush: #f2a0a8;
  }
  * { margin: 0; padding: 0; box-sizing: border-box; }
  html, body { width: 1200px; height: 1200px; overflow: hidden; background: var(--backdrop); }
  .poster {
    position: absolute; left: 203px; top: 40px;
    width: 814px; height: 1150px;
    transform: scale(0.974); transform-origin: 0 0;
    background: linear-gradient(120deg, var(--sky-light) 0%, var(--sky-mid) 60%, #c8def3 100%);
    overflow: hidden;
  }
  .hero-photo {
    position: absolute; left: 398px; top: 0; width: 416px; height: 988px;
    background:
      radial-gradient(ellipse 55% 40% at 60% 78%, rgba(242,140,150,0.75), rgba(242,140,150,0) 70%),
      radial-gradient(ellipse 45% 30% at 70% 50%, rgba(250,215,220,0.8), rgba(250,215,220,0) 70%),
      linear-gradient(90deg, rgba(220,236,249,0) 0%, var(--sky-deep) 100%);
  }
  .title {
    position: absolute; left: 43px; top: 72px;
    font-family: "Roboto Slab", serif; font-weight: 700;
    font-size: 70px; line-height: 83px; color: var(--brand-blue);
    letter-spacing: 1px;
  }
  .subtitle {
    position: absolute; left: 44px; top: 242px;
    font-family: "Lexend", sans-serif; font-weight: 500;
    font-size: 46px; line-height: 55px; color: var(--ink);
  }
  .promo-lead {
    position: absolute; left: 48px; top: 418px;
    font-family: "Roboto Slab", serif; font-weight: 500;
    font-size: 30px; line-height: 40px; color: var(--ink);
  }
  .discount {
    position: absolute; left: 44px; top: 492px;
    font-family: "Roboto Condensed", sans-serif; font-weight: 700;
    color: var(--brand-blue-dark); white-space: nowrap;
  }
  .discount .value { font-size: 118px; letter-spacing: -2px; }
  .discount .unit { font-size: 72px; margin-left: 8px; }
  .package {
    position: absolute; left: 47px; top: 612px;
    font-family: "Roboto", sans-serif; font-weight: 500;
    font-size: 28px; color: var(--ink);
  }
  .event {
    position: absolute; left: 48px; top: 714px;
    font-family: "Roboto", sans-serif; font-weight: 500;
    font-size: 32px; line-height: 40px; color: var(--ink);
  }
  .event .place { color: var(--brand-blue-dark); }
  .contacts {
    position: absolute; left: 50px; top: 838px; list-style: none;
    font-family: "Roboto Slab", serif; font-weight: 500;
    font-size: 20px; color: var(--ink);
  }
  .contacts li { display: flex; align-items: center; height: 41px; }
  .contacts svg { width: 26px; height: 26px; margin-right: 12px; flex: none; }
  .footer-band { position: absolute; left: 0; top: 988px; width: 814px; height: 162px; }
  .brand {
    position: absolute; left: 44px; top: 1043px;
    display: flex; align-items: center;
    font-family: "Roboto Slab", serif; font-weight: 400;
    font-size: 36px; color: var(--white);
  }
  .brand .mark { width: 34px; height: 34px; border-radius: 50%; background: var(--white); margin-right: 18px; }
  .tagline {
    position: absolute; left: 524px; top: 1090px;
    font-family: "Roboto", sans-serif; font-weight: 500;
    font-size: 19px; letter-spacing: 4px; color: var(--gold); text-transform: uppercase;
  }
</style>
</head>
<body>
  <main class="poster">
    <div class="hero-photo" role="img" aria-label="Photo of a smiling pregnant woman in a striped top and pink skirt, holding her belly"></div>

    <h1 class="title">PREGNANT<br>CLASS</h1>
    <h2 class="subtitle">Eating healthy<br>while pregnant</h2>

    <p class="promo-lead">Promote when<br>join in out class:</p>
    <p class="discount"><span class="value">30%</span><span class="unit">off</span></p>
    <p class="package">DELIVERY PACKAGE</p>

    <p class="event"><span class="place">SINGAPORE -</span><br>25.11.2018</p>

    <ul class="contacts">
      <li>
        <svg viewBox="0 0 24 24" fill="none" stroke="#2a8fc4" stroke-width="1.8" stroke-linecap="round" stroke-linejoin="round"><path d="M5 4h3l2 5-2 1.5a11 11 0 0 0 5.5 5.5L15 14l5 2v3a2 2 0 0 1-2 2A16 16 0 0 1 3 6a2 2 0 0 1 2-2z"/><path d="M15 3a6 6 0 0 1 6 6"/><path d="M15 6.5a2.5 2.5 0 0 1 2.5 2.5"/></svg>
        +65 6100 2468
      </li>
      <li>
        <svg viewBox="0 0 24 24" fill="none" stroke="#2a8fc4" stroke-width="1.8" stroke-linejoin="round"><rect x="2" y="5" width="20" height="14"/><path d="M2 5l10 8 10-8M2 19l7.5-7M22 19l-7.5-7"/></svg>
        care@harbourvalehealth.com
      </li>
      <li>
        <svg viewBox="0 0 24 24" fill="none" stroke="#2a8fc4" stroke-width="1.6"><circle cx="12" cy="12" r="10"/><ellipse cx="12" cy="12" rx="4.5" ry="10"/><path d="M2 12h20M4 7h16M4 17h16"/></svg>
        www.harbourvalehospital.com.sg
      </li>
    </ul>

    <svg class="footer-band" viewBox="0 0 814 162" aria-hidden="true">
      <rect width="814" height="162" fill="var(--white)"/>
      <polygon points="0,0 568,0 443,162 0,162" fill="var(--gold)"/>
    </svg>
    <div class="brand"><span class="mark"></span>Harbourvale</div>
    <p class="tagline">Care made close.</p>
  </main>
</body>
</html>
```